TULVAN COFFEE Menu Re-Design (drive-thru coffee shop)

* Keep style of old menu and fonts

* Change to new layout with orange outlines around each product section. I want the orange outlines to look like the orange circle around the "tax not included" on the old menu. I've attached "NEW menu layout 1" for reference.

* Change to new layout, products, sizes, and prices. I attached "Tulvan Menu NEW" for reference.

* Change background color of menu from dark blue to light/medium grey

* Change to new logo (my attachment has 3 logos. Use the top/1st logo please).

Let me know if there are any questions about anything or if you need different file types.

Thank you!

Industry/Entity Type

Coffee

Font styles to use
Other font styles liked:
• High Voltage (I've attached the font in the brief.)

Colors
F0912C
F2A743
F7CA91
FBE8D2
FDF5EE

Requirements
Must have
• Grey, Orange and White theme.
Should not have
• The color black

```html
<!DOCTYPE html>
<html lang="en">
<head>
<meta charset="utf-8">
<title>Tulvan Coffee Menu</title>
<link href="https://fonts.googleapis.com/css2?family=Bebas+Neue&family=Oswald:wght@400;500&display=swap" rel="stylesheet">
<style>
  :root {
    --board: #5d6063;
    --chalk: #fdf5ee;
    --chalk-soft: #fbe8d2;
    --orange: #f0912c;
    --orange-light: #f2a743;
    --outline: #f0912c;
  }
  * { box-sizing: border-box; margin: 0; padding: 0; }
  html, body { width: 848px; height: 1200px; overflow: hidden; }
  body {
    background: var(--board);
    font-family: "Oswald", "Arial Narrow", sans-serif;
    color: var(--chalk);
  }
  .menu-board { position: relative; width: 848px; height: 1200px; background: var(--board); }
  .rules { position: absolute; inset: 0; }
  .rules line, .rules rect, .rules ellipse { stroke: var(--outline); fill: none; stroke-linecap: round; }

  .block { position: absolute; white-space: nowrap; }
  .heading {
    font-family: "Bebas Neue", "Oswald", sans-serif;
    color: var(--orange);
    font-size: 21px;
    line-height: 1;
    letter-spacing: .3px;
  }
  .note {
    font-family: "Bebas Neue", "Oswald", sans-serif;
    color: var(--orange-light);
    font-size: 14px;
    line-height: 1;
    letter-spacing: .3px;
  }
  .item { font-size: 10.5px; line-height: 13px; text-transform: uppercase; letter-spacing: .2px; color: var(--chalk); }
  .orange { color: var(--orange); }

  .side-label {
    position: absolute;
    writing-mode: vertical-rl;
    transform: rotate(180deg);
    font-family: "Bebas Neue", "Oswald", sans-serif;
    color: var(--orange);
    line-height: 1;
    text-align: center;
    white-space: nowrap;
  }

  .grid { display: grid; }
  .size-pair { display: flex; flex-direction: column; }
  .stack { display: flex; flex-direction: column; }
  .syrup-col { display: flex; flex-direction: column; gap: 7.5px; width: 112px; white-space: normal; }
  .center { text-align: center; }

  .brand { position: absolute; left: 324px; top: 76px; width: 200px; text-align: center; }
  .brand-name {
    font-family: "Bebas Neue", "Oswald", sans-serif;
    color: var(--orange);
    font-size: 40px;
    line-height: 40px;
    letter-spacing: 1px;
  }
  .brand-place { font-size: 9px; letter-spacing: 2px; color: var(--chalk); margin-top: 4px; }

  .sizes-bar { position: absolute; left: 102px; top: 1166px; display: flex; align-items: baseline; gap: 6px; white-space: nowrap; }
  .sizes-bar .heading { font-size: 19px; margin-right: 6px; }
  .sizes-bar .item { font-size: 10.5px; }
  .sizes-bar .gap { width: 22px; }
</style>
</head>
<body>
<main class="menu-board">

  <svg class="rules" width="848" height="1200" viewBox="0 0 848 1200" aria-hidden="true">
    <rect x="23" y="17" width="803" height="1174" stroke-width="1.8"/>
    <line x1="25" y1="139" x2="324" y2="137" stroke-width="2.2"/>
    <line x1="324" y1="137" x2="326" y2="324" stroke-width="2.2"/>
    <line x1="23" y1="332" x2="328" y2="330" stroke-width="2.2"/>
    <line x1="507" y1="137" x2="822" y2="137" stroke-width="2"/>
    <line x1="507" y1="137" x2="507" y2="302" stroke-width="2"/>
    <line x1="512" y1="302" x2="824" y2="300" stroke-width="2.2"/>
    <ellipse cx="413" cy="292" rx="75" ry="99" stroke-width="2.2"/>
    <line x1="23" y1="436" x2="825" y2="436" stroke-width="2"/>
    <line x1="88" y1="648" x2="822" y2="648" stroke-width="2"/>
    <line x1="227" y1="664" x2="228" y2="752" stroke-width="1.6"/>
    <line x1="416" y1="664" x2="417" y2="752" stroke-width="1.6"/>
    <line x1="23" y1="760" x2="825" y2="760" stroke-width="2"/>
    <line x1="319" y1="780" x2="320" y2="850" stroke-width="1.6"/>
    <line x1="573" y1="780" x2="572" y2="850" stroke-width="1.6"/>
    <line x1="23" y1="859" x2="825" y2="859" stroke-width="2"/>
    <line x1="433" y1="870" x2="434" y2="960" stroke-width="1.6"/>
    <line x1="88" y1="967" x2="825" y2="967" stroke-width="2"/>
    <line x1="268" y1="975" x2="269" y2="1058" stroke-width="1.6"/>
    <line x1="497" y1="975" x2="498" y2="1058" stroke-width="1.6"/>
    <line x1="23" y1="1066" x2="825" y2="1066" stroke-width="2"/>
    <line x1="262" y1="1080" x2="263" y2="1155" stroke-width="1.6"/>
    <line x1="535" y1="1080" x2="534" y2="1155" stroke-width="1.6"/>
    <line x1="23" y1="1160" x2="825" y2="1160" stroke-width="2"/>
  </svg>

  <header class="brand">
    <div class="brand-name">TULVAN COFFEE</div>
    <div class="brand-place">HARLAN · TEXAS</div>
  </header>

  <div class="side-label" style="left:32px;top:184px;width:46px;height:117px;font-size:50px;">COFFEE</div>

  <section class="block" style="left:98px;top:147px;">
    <span class="heading">Espresso</span>
    <span class="note" style="margin-left:48px;">Add any flavors</span>
  </section>
  <div class="block grid espresso-table" style="left:98px;top:177px;grid-template-columns:84px 52px 50px 40px;grid-auto-rows:19.5px;">
    <span class="item orange">Hot | Iced</span><span class="item">Small</span><span class="item">Medium</span><span class="item">Large</span>
    <span class="item">Mocha</span><span class="item">3.95</span><span class="item">4.45</span><span class="item">5.45</span>
    <span class="item">Latte</span><span class="item">3.95</span><span class="item">4.45</span><span class="item">5.45</span>
    <span class="item">Breve</span><span class="item">3.95</span><span class="item">4.45</span><span class="item">5.45</span>
    <span class="item">Macchiato</span><span class="item">3.95</span><span class="item">4.45</span><span class="item">5.45</span>
    <span class="item">Cappucino</span><span class="item">3.70</span><span class="item">4.20</span><span class="item">5.20</span>
    <span class="item">Americano</span><span class="item">2.45</span><span class="item">2.95</span><span class="item">3.95</span>
    <span class="item">Espresso</span><span class="item">1.50</span><span></span><span></span>
  </div>

  <section class="block" style="left:98px;top:344px;">
    <div class="heading">Cold Brew | Nitro Cold Brew</div>
    <div class="note" style="margin-top:6px;">Add any flavor | Add cold foam +.50</div>
  </section>
  <div class="block grid" style="left:98px;top:400px;grid-template-columns:82px 82px 80px;">
    <div class="size-pair"><span class="item">Small | 16oz</span><span class="item">$3.75</span></div>
    <div class="size-pair"><span class="item">Medium | 24oz</span><span class="item">$4.25</span></div>
    <div class="size-pair"><span class="item">Large | 32oz</span><span class="item">$4.75</span></div>
  </div>

  <section class="block center" style="left:338px;top:237px;width:150px;">
    <div class="heading">Drip Coffee</div>
    <div class="stack" style="margin-top:14px;gap:8px;">
      <div class="size-pair"><span class="item">Small | 16oz</span><span class="item">$1.75</span></div>
      <div class="size-pair"><span class="item">Medium | 24oz</span><span class="item">$2.25</span></div>
      <div class="size-pair"><span class="item">Large | 32oz</span><span class="item">$2.75</span></div>
    </div>
  </section>

  <section class="block" style="left:521px;top:147px;">
    <div class="heading">Frozen Espresso</div>
  </section>
  <div class="block grid" style="left:521px;top:175px;grid-template-columns:80px 111px 110px;">
    <div class="size-pair"><span class="item">Small | 16oz</span><span class="item">$4.75</span></div>
    <div class="size-pair"><span class="item">Medium | 24oz</span><span class="item">$5.75</span></div>
    <div class="size-pair"><span class="item">Large | 32oz</span><span class="item">$6.75</span></div>
  </div>
  <div class="block grid" style="left:521px;top:214px;grid-template-columns:80px 111px 110px;grid-auto-rows:21px;">
    <span class="item">Vanilla Bean</span><span class="item">White Chocolate</span><span class="item">Mint Chocolate Chip</span>
    <span class="item">Nougat Crunch</span><span class="item">Peanut Cup</span><span class="item">NSA Vanilla Bean</span>
    <span class="item">Mocha</span><span class="item">Caramel Meltdown</span><span class="item">Cookies &amp; Cream</span>
    <span class="item">Crispy Peanut</span><span class="item">Coconut Almond</span><span class="item">NSA Mocha</span>
  </div>

  <section class="block" style="left:533px;top:313px;">
    <div class="heading">Dairy Free +$.50</div>
    <div class="item" style="margin-top:6px;word-spacing:4px;">Almond | Soy | Oat | Coconut</div>
  </section>
  <section class="block" style="left:533px;top:367px;">
    <div class="heading">Add-On's</div>
  </section>
  <div class="block grid" style="left:533px;top:393px;grid-template-columns:110px 130px;grid-auto-rows:21px;">
    <span class="item">Espresso Shot | $.50</span><span class="item">Whipped Cream | Free</span>
    <span class="item">Extra Flavor | Free</span><span class="item">Sweet Cream Cold Foam | $.50</span>
  </div>

  <div class="side-label" style="left:28px;top:462px;width:46px;height:272px;font-size:44px;">Syrups &amp; Sauces</div>

  <div class="block heading center" style="left:374px;top:444px;width:100px;">Syrups</div>
  <div class="block grid" style="left:127px;top:472px;grid-template-columns:118px 117px 118px 117px 118px 100px;">
    <div class="syrup-col">
      <span class="item">Almond</span><span class="item">Almond Brittle</span><span class="item">Amaretto</span>
      <span class="item">Brown Sugar<br>Cinnamon</span><span class="item">Butter Pecan</span><span class="item">Butter Rum</span>
      <span class="item">Butterscotch</span><span class="item">Caramel</span>
    </div>
    <div class="syrup-col">
      <span class="item">Cheesecake</span><span class="item">Cookie Dough</span><span class="item">Cinnamon</span>
      <span class="item">Cupcake</span><span class="item">English Toffee</span><span class="item">Hazelnut</span>
      <span class="item">Hibiscus</span><span class="item">Irish Cream</span>
    </div>
    <div class="syrup-col">
      <span class="item">Lavender</span><span class="item">Macadamia Nut</span><span class="item">Maple</span>
      <span class="item">Peppermint</span><span class="item">Salted Caramel</span><span class="item">Shortbread</span>
      <span class="item">Toasted<br>Marshmallow</span><span class="item">Vanilla Bean</span>
    </div>
    <div class="syrup-col">
      <span class="item">Apple</span><span class="item">Grapefruit</span><span class="item">Passion Fruit</span>
      <span class="item">Banana</span><span class="item">Green Apple</span><span class="item">Peach</span>
      <span class="item">Blackberry</span><span class="item">Guava</span>
    </div>
    <div class="syrup-col">
      <span class="item">Pineapple</span><span class="item">Blueberry</span><span class="item">Kiwi</span>
      <span class="item">Pomegranate</span><span class="item">Blueberry</span><span class="item">Lemon</span>
      <span class="item">Raspberry</span><span class="item">Cherry</span>
    </div>
    <div class="syrup-col">
      <span class="item">Lime</span><span class="item">Strwberry</span><span class="item">Coconut</span>
      <span class="item">Mango</span><span class="item">Watermelon</span><span class="item">Grape</span>
      <span class="item">Orange</span>
    </div>
  </div>

  <section class="block" style="left:127px;top:658px;">
    <div class="heading">Sauces</div>
    <div class="stack" style="margin-top:4px;gap:8px;">
      <span class="item">Chocolate</span><span class="item">White Chocolate</span><span class="item">Caramel</span>
    </div>
  </section>
  <section class="block" style="left:248px;top:658px;">
    <div class="heading">Sugar Free Sauces</div>
    <div class="stack" style="margin-top:4px;gap:8px;">
      <span class="item">Chocolate</span><span class="item">White Chocolate</span><span class="item">Caramel</span>
    </div>
  </section>
  <section class="block" style="left:442px;top:658px;">
    <div class="heading">Sugar Free Syrups</div>
  </section>
  <div class="block grid" style="left:442px;top:680px;grid-template-columns:90px 94px;grid-auto-rows:21px;">
    <span class="item">Almond Brittle</span><span class="item">Irish Cream</span>
    <span class="item">Caramel</span><span class="item">Peppermint</span>
    <span class="item">English Toffee</span><span class="item">Salted Caramel</span>
    <span class="item">Hazelnut</span><span class="item">Vanilla Bean</span>
  </div>
  <div class="block grid" style="left:626px;top:659px;grid-template-columns:92px 90px;grid-auto-rows:21px;">
    <span class="item">Blue Raspberry</span><span class="item">Orange</span>
    <span class="item">Coconut</span><span class="item">Peach</span>
    <span class="item">Lemon</span><span class="item">Raspberry</span>
    <span class="item">Lime</span><span class="item">Strwberry</span>
    <span class="item">Mango</span><span class="item">Watermelon</span>
  </div>

  <div class="side-label" style="left:33px;top:780px;width:46px;height:62px;font-size:50px;">Tea</div>

  <section class="block" style="left:107px;top:767px;">
    <span class="heading">Chai</span>
    <span class="note" style="margin-left:4px;">Hot | Iced +$.50 | Frozen +$1</span>
  </section>
  <div class="block grid" style="left:107px;top:792px;grid-template-columns:60px 75px 70px;">
    <div class="size-pair"><span class="item">Small</span><span class="item">$3.75</span></div>
    <div class="size-pair"><span class="item">Medium</span><span class="item">$4.50</span></div>
    <div class="size-pair"><span class="item">Large</span><span class="item">$5.50</span></div>
  </div>
  <div class="block grid" style="left:107px;top:824px;grid-template-columns:60px 75px 70px;grid-auto-rows:18px;">
    <span class="item">Spiced</span><span class="item">Chocolate</span><span class="item">Raspberry</span>
    <span class="item">Vanilla</span><span class="item">NSA Vanilla</span><span></span>
  </div>

  <section class="block" style="left:334px;top:767px;">
    <div class="heading">Hot Tea</div>
  </section>
  <div class="block grid" style="left:334px;top:792px;grid-template-columns:82px 82px 70px;">
    <div class="size-pair"><span class="item">Small | 12oz</span><span class="item">$2.25</span></div>
    <div class="size-pair"><span class="item">Medium | 16oz</span><span class="item">$2.75</span></div>
    <div class="size-pair"><span class="item">Large | 20oz</span><span class="item">$2.95</span></div>
  </div>
  <div class="block grid" style="left:334px;top:824px;grid-template-columns:96px 53px 90px;grid-auto-rows:18px;">
    <span class="item">English Breakfast</span><span class="item">Earl Grey</span><span class="item">Sweet Cinnamon</span>
    <span class="item">Green Tea</span><span class="item">Mint</span><span class="item">Peach</span>
  </div>

  <section class="block" style="left:583px;top:767px;">
    <span class="heading">Iced Tea</span>
    <span class="note" style="margin-left:12px;">Add any flavor</span>
  </section>
  <div class="block grid" style="left:583px;top:792px;grid-template-columns:77px 75px 70px;">
    <div class="size-pair"><span class="item">Small | 16oz</span><span class="item">$2.95</span></div>
    <div class="size-pair"><span class="item">Medium | 24oz</span><span class="item">$3.25</span></div>
    <div class="size-pair"><span class="item">Large | 32oz</span><span class="item">$3.50</span></div>
  </div>
  <div class="block grid" style="left:583px;top:824px;grid-template-columns:77px 75px;">
    <span class="item">Black Tea</span><span class="item">Green Tea</span>
  </div>

  <div class="side-label" style="left:30px;top:876px;width:24px;height:176px;font-size:22px;text-align:start;">Tulvan Energy Sodas</div>
  <div class="side-label" style="left:60px;top:876px;width:18px;height:176px;font-size:16px;text-align:start;">Iced | Frozen</div>

  <section class="block" style="left:98px;top:868px;">
    <div class="heading">Brightfruit Smoothies</div>
  </section>
  <div class="block grid" style="left:98px;top:892px;grid-template-columns:118px 91px 90px;">
    <div class="size-pair"><span class="item">Small | 16oz</span><span class="item">$5.75</span></div>
    <div class="size-pair"><span class="item">Medium | 24oz</span><span class="item">$6.75</span></div>
    <div class="size-pair"><span class="item">Large | 32oz</span><span class="item">$7.75</span></div>
  </div>
  <div class="block grid" style="left:98px;top:924px;grid-template-columns:118px 91px 90px;grid-auto-rows:21px;">
    <span class="item">Strawberry</span><span class="item">Peach</span><span class="item">Superfruit</span>
    <span class="item">Strawberry Banana</span><span class="item">Mango</span><span class="item">Tropical</span>
  </div>

  <section class="block" style="left:505px;top:868px;">
    <span class="heading">Handcrafted Lemonade</span>
    <span class="note" style="margin-left:4px;">Iced | Frozen +$.50</span>
  </section>
  <div class="block grid" style="left:505px;top:892px;grid-template-columns:96px 90px 80px;">
    <div class="size-pair"><span class="item">Small | 16oz</span><span class="item">$2.75</span></div>
    <div class="size-pair"><span class="item">Medium | 24oz</span><span class="item">$3.25</span></div>
    <div class="size-pair"><span class="item">Large | 32oz</span><span class="item">$4.00</span></div>
  </div>
  <div class="block grid" style="left:505px;top:924px;grid-template-columns:96px 90px 80px;grid-auto-rows:21px;">
    <span class="item">Original</span><span class="item">Blackberry</span><span class="item">Peach</span>
    <span class="item">Blue Raspberry</span><span class="item">Strawberry</span><span class="item">Cherry</span>
  </div>

  <section class="block" style="left:100px;top:973px;">
    <div class="heading">Red Rally</div>
    <div class="note" style="margin-top:2px;">Iced | Frozen</div>
  </section>
  <div class="block grid" style="left:100px;top:1016px;grid-template-columns:77px 70px;">
    <div class="stack"><span class="item">Small | 24oz</span><span class="item" style="margin-top:2px;">1 Can</span><span class="item" style="margin-top:2px;">$5.95</span></div>
    <div class="stack"><span class="item">Large | 32oz</span><span class="item" style="margin-top:2px;">2 Cans</span><span class="item" style="margin-top:2px;">$7.95</span></div>
  </div>

  <section class="block center" style="left:300px;top:978px;width:176px;">
    <div class="heading">Lumen Plant Energy</div>
    <div class="note" style="margin-top:2px;">Iced | Frozen</div>
  </section>
  <div class="block grid" style="left:311px;top:1022px;grid-template-columns:81px 70px;">
    <div class="size-pair"><span class="item">Small | 24oz</span><span class="item">$5.75</span></div>
    <div class="size-pair"><span class="item">Large | 32oz</span><span class="item">$6.75</span></div>
  </div>

  <section class="block" style="left:534px;top:978px;">
    <div class="heading">Infuse with any fruit flavors</div>
    <div class="stack" style="margin-top:6px;gap:3px;">
      <span class="item">Add Topper:</span>
      <span class="item">Whipped Cream | Cream | Sweet Cream Cold Foam</span>
      <span class="item">Orange Juice +$.50 | Lemonade +$.50</span>
    </div>
  </section>

  <section class="block center" style="left:32px;top:1073px;width:222px;">
    <div class="heading">Hot Chocolate</div>
    <div class="note" style="margin-top:2px;">Try a "Frozen" hot chocolate +$.50</div>
    <div class="note" style="margin-top:2px;">Add any flavor</div>
    <div class="grid" style="grid-template-columns:1fr 1fr 1fr;margin-top:2px;">
      <div class="size-pair"><span class="item">Small</span><span class="item">$2.75</span></div>
      <div class="size-pair"><span class="item">Medium</span><span class="item">$3.25</span></div>
      <div class="size-pair"><span class="item">Large</span><span class="item">$3.75</span></div>
    </div>
  </section>

  <section class="block center" style="left:270px;top:1073px;width:260px;">
    <div class="heading">Italian Sodas</div>
    <div class="note" style="margin-top:2px;">Infuse with any flavors</div>
    <div class="note" style="margin-top:2px;">With or without cream</div>
    <div class="grid" style="grid-template-columns:1fr 1fr 1fr;margin-top:2px;">
      <div class="size-pair"><span class="item">Small | 16oz</span><span class="item">$2.95</span></div>
      <div class="size-pair"><span class="item">Medium | 24oz</span><span class="item">$3.45</span></div>
      <div class="size-pair"><span class="item">Large | 32oz</span><span class="item">$3.95</span></div>
    </div>
  </section>

  <section class="block center" style="left:545px;top:1073px;width:256px;">
    <div class="heading">Kids</div>
    <div class="note" style="margin-top:2px;">All drinks come with whip cream</div>
    <div class="note" style="margin-top:2px;">and sprinkles</div>
    <div class="item" style="margin-top:2px;">Brightfruit Smoothie | Any Flavor $2.95</div>
    <div class="item" style="margin-top:3px;">Steamer | Any Flavor + Warm Steamed Milk $2.25</div>
  </section>

  <footer class="sizes-bar">
    <span class="heading">Sizes:</span>
    <span class="item">Hot</span><span class="item">|</span>
    <span class="item orange">Small</span><span class="item">| 12oz</span>
    <span class="item orange">Medium</span><span class="item">| 16oz</span>
    <span class="item orange">Large</span><span class="item">| 20oz</span>
    <span class="gap"></span>
    <span class="item">Cold</span><span class="item">|</span>
    <span class="item orange">Small</span><span class="item">| 16oz</span>
    <span class="item orange">Medium</span><span class="item">| 24oz</span>
    <span class="item orange">Large</span><span class="item">| 32oz</span>
  </footer>

</main>
</body>
</html>
```